Letterhead Design Project

Looking for letterhead designs for Brastova Mining.

I am looking for a letterhead design in conjunction with a business card design. I have opened contests for both but ask that if you submit a letterhead design you also submit a business card design with a corresponding look/feel.

Brastova Mining is a B2B company that buys and sells large machinery tires within the coal mining industry. The design should the strong, crisp and masculine. I have uploaded the company logo and mock-up of the back of the company's business card.

Color scheme should be grey/green/black

Contact information to include:
Name: Dale Whitford
Title: Managing Director
Phone: 555-231-4097
Address: 1817 Pellam #3 Dallas, TX 75290
Email: Dale@Brastova.example
Updates

Project Deadline Extended
Reason: Looking for a more refined, elegant letterhead than what's been submitted as of yet. Here is a sample of what we're looking for: http://www.plumcrestgallery.example/letterhead-designs/ We will also be increasing the payment.

Industry/Entity Type

Coal Mining

```html
<!DOCTYPE html>
<html lang="en">
<head>
<meta charset="utf-8">
<title>Brastova Mining Letterhead</title>
<link href="https://fonts.googleapis.com/css2?family=Arimo:wght@400;700&display=swap" rel="stylesheet">
<style>
  :root {
    --green: #5da944;
    --green-light: #cae3b4;
    --charcoal: #58595b;
    --text: #231f20;
    --muted: #4d4d4f;
    --page-edge: #9a9a9a;
    --backdrop: #ffffff;
  }
  * { box-sizing: border-box; margin: 0; padding: 0; }
  html, body {
    width: 1200px;
    height: 1000px;
    overflow: hidden;
    background: var(--backdrop);
    font-family: "Arimo", Arial, sans-serif;
  }
  .sheet {
    position: absolute;
    left: 233px;
    top: 25px;
    width: 734px;
    height: 951px;
    background: #fff;
    border: 1px solid var(--page-edge);
    box-shadow: 6px 6px 10px rgba(0,0,0,0.18);
  }
  .masthead {
    position: absolute;
    top: 92px;
    left: 0;
    width: 100%;
    text-align: center;
  }
  .brand {
    display: inline-flex;
    align-items: center;
    gap: 8px;
    font-size: 25px;
    font-weight: 700;
    color: var(--charcoal);
    letter-spacing: 0.5px;
  }
  .brand-mark {
    width: 14px;
    height: 14px;
    background: var(--green);
  }
  .sender {
    margin-top: 48px;
    font-size: 9.5px;
    line-height: 11.5px;
    color: var(--muted);
  }
  .sender .dot { color: var(--green); margin: 0 4px; }
  .recipient-band {
    position: absolute;
    top: 215px;
    left: 0;
    width: 100%;
    height: 102px;
    display: flex;
  }
  .recipient {
    width: 286px;
    background: var(--green);
    color: #fff;
    font-size: 11.5px;
    line-height: 14.4px;
    padding: 9px 0 0 86px;
  }
  .recipient-band .accent {
    flex: 1;
    background: var(--green-light);
  }
  .letter-body {
    position: absolute;
    top: 344px;
    left: 86px;
    width: 566px;
    font-size: 11.3px;
    line-height: 14.4px;
    color: var(--text);
  }
  .letter-body p + p { margin-top: 14.4px; }
  .footer {
    position: absolute;
    left: 0;
    bottom: 0;
    width: 100%;
    height: 44px;
    background: var(--green);
    color: #fff;
    font-size: 9.5px;
    display: flex;
    align-items: center;
    justify-content: center;
    padding-bottom: 18px;
  }
  .footer .sep { margin: 0 6px; }
</style>
</head>
<body>
  <div class="sheet">
    <header class="masthead">
      <div class="brand"><span class="brand-mark"></span>Brastova Mining</div>
      <div class="sender">
        <div>Dale Whitford<span class="dot">•</span>Managing Director</div>
        <div>(555) 231-4097</div>
        <div>Dale@Brastova.example</div>
      </div>
    </header>

    <section class="recipient-band">
      <div class="recipient">
        To:<br>
        Recipient Name<br>
        Recipient Address 1<br>
        Recipient Address 2<br>
        Recipient Phone<br>
        Recipient E-Mail
      </div>
      <div class="accent"></div>
    </section>

    <main class="letter-body">
      <p>Lorem ipsum dolor sit amet, consectetur adipiscing elit. Nam condimentum volutpat tempus. Sed velit augue, faucibus eget eleifend sed, luctus in tellus. Etiam justo magna, molestie quis tempor sit amet, interdum eget sem. Sed nec cursus lacus. Nulla facilisi. Vestibulum ante ipsum primis in faucibus orci luctus et ultrices posuere cubilia Curae; Maecenas hendrerit sed lectus ut molestie. Cras nec urna sit amet nibh semper rutrum. Interdum et malesuada fames ac ante ipsum primis in faucibus. Quisque urna augue, ornare quis mattis et, luctus a mi. Proin sed lobortis sem. Nullam tempor euismod lectus, auctor vulputate purus convallis sit amet. Sed enim augue, fringilla eu pellentesque nec, porttitor vitae mauris. Aenean a eros lacus. Sed non diam mi.</p>
      <p>Aliquam ut tellus pulvinar, scelerisque nulla eget, viverra nisl. Class aptent taciti sociosqu ad litora torquent per conubia nostra, per inceptos himenaeos. Nulla at elit dui. Nunc risus risus, viverra ut orci et, hendrerit placerat elit. In non nunc ornare, vehicula ligula nec, iaculis dolor. Proin congue lectus sit amet sapien tempor dignissim. Duis molestie quis erat sed placerat. Pellentesque non varius ipsum. Donec vulputate ipsum lorem, a feugiat quam luctus sit amet. Sed pulvinar lectus vel erat tristique tristique. Quisque enim eros, mattis vel eleifend non, aliquam nec ligula. Nullam fringilla sed felis nec porta.</p>
      <p>Proin sollicitudin velit eros, vel pharetra mi commodo ut. Donec sit amet massa non justo sollicitudin faucibus. Morbi fringilla orci elit, sed egestas est dignissim mollis. In dapibus dictum faucibus. Praesent mollis, est convallis posuere cursus, massa nunc porta justo, ac commodo metus quam ac purus. Sed sapien tortor, dignissim bibendum elit sed, rutrum suscipit nunc. Sed eget purus urna. Sed euismod massa sed mauris viverra, nec commodo magna aliquet. Nullam vitae arcu sed quam consectetur congue. Aliquam luctus suscipit nibh at volutpat.</p>
      <p>Nam vulputate augue non leo pharetra, vel cursus nisi varius. Donec placerat convallis justo sit amet ullamcorper. Nullam a tellus sed risus vestibulum sollicitudin. Proin magna nisl, feugiat vitae metus sit amet, condimentum consequat sem. Aenean condimentum id orci vitae malesuada. Praesent gravida dui non tortor dapibus, sed dignissim magna condimentum. Nullam volutpat lacinia risus at venenatis. Sed ornare sodales dui a ornare. Integer imperdiet gravida posuere. Curabitur suscipit convallis sollicitudin. Suspendisse lorem lacus, rutrum sed eleifend non, luctus et elit. Praesent in aliquam ipsum.</p>
      <p>Aenean quis facilisis sem. Ut euismod eros a quam mattis dignissim. Praesent nec eros non lacus cursus sodales ut ac augue. Cras luctus, ligula eget viverra hendrerit, enim leo aliquam elit, eget feugiat neque nibh eget risus. Quisque non tincidunt lorem. Suspendisse non mattis justo, in hendrerit nulla. Vestibulum justo turpis, rhoncus nec nisl ut, ultricies sagittis nulla. Donec blandit sollicitudin pulvinar.</p>
    </main>

    <footer class="footer">
      <span>Brastova Mining</span><span class="sep">•</span>
      <span>1817 Pellam Street, #3 Dallas, TX 75290</span><span class="sep">•</span>
      <span>(555) 231-4097</span><span class="sep">•</span>
      <span>www.brastova.example</span>
    </footer>
  </div>
</body>
</html>
```